BRL Design Business Card

I need to develop a business card for my real estate design and investment company. Something clean, classic and professional with a modern vibe.

Industry/Entity Type

Real Estate

Font styles to use
Serif
Sans Serif

```html
<!DOCTYPE html>
<html lang="en">
<head>
<meta charset="UTF-8">
<title>BRL Design Business Card</title>
<link href="https://fonts.googleapis.com/css2?family=Jost:wght@300;400;500&display=swap" rel="stylesheet">
<style>
  :root {
    --backdrop: #262626;
    --card-light: #ffffff;
    --card-dark: #3a3a3a;
    --ink: #2b2b2b;
    --ink-soft: #555555;
    --band: #3d3d3d;
    --paper-text: #f2f2f2;
    --ghost: #474747;
  }
  * { margin: 0; padding: 0; box-sizing: border-box; }
  html, body { width: 1200px; height: 1200px; overflow: hidden; }
  body {
    background: var(--backdrop);
    font-family: "Jost", "Helvetica Neue", Arial, sans-serif;
    position: relative;
  }
  .card {
    position: absolute;
    width: 700px;
    height: 390px;
    border-radius: 18px;
    overflow: hidden;
    box-shadow: 0 10px 30px rgba(0,0,0,0.45);
  }
  /* Front */
  .card-front { left: 130px; top: 120px; background: var(--card-light); color: var(--ink); }
  .brand {
    position: absolute;
    display: flex;
    flex-direction: column;
    align-items: flex-start;
  }
  .brand-name {
    font-weight: 300;
    letter-spacing: 6px;
    line-height: 1;
  }
  .brand-tagline { font-weight: 400; }
  .card-front .brand { left: 95px; top: 120px; }
  .card-front .brand-name { font-size: 78px; color: var(--ink); }
  .card-front .brand-tagline { font-size: 15px; color: var(--ink); margin-top: 4px; }
  .divider {
    position: absolute;
    left: 328px; top: 40px;
    width: 2px; height: 235px;
    background: linear-gradient(to bottom, rgba(40,40,40,0), rgba(40,40,40,0.85) 60%, rgba(40,40,40,0.2));
  }
  .contact { position: absolute; left: 355px; top: 40px; }
  .person-name { font-size: 27px; font-weight: 500; line-height: 1.1; }
  .person-role { font-size: 17px; color: var(--ink-soft); margin: 2px 0 22px 6px; }
  .contact-list { list-style: none; }
  .contact-item {
    display: flex; align-items: center; gap: 10px;
    font-size: 19px; line-height: 1.45; color: var(--ink);
  }
  .contact-item svg { width: 15px; height: 15px; flex: none; }
  .address-band {
    position: absolute; left: 0; right: 0; top: 292px; height: 42px;
    background: var(--band);
    color: var(--paper-text);
    font-size: 19px; letter-spacing: 0.5px;
    display: flex; align-items: center; justify-content: flex-end;
    padding-right: 40px;
  }
  /* Back */
  .card-back { left: 370px; top: 660px; background: var(--card-dark); }
  .card-back .brand { left: 55px; top: 125px; z-index: 1; }
  .card-back .brand-name { font-size: 96px; color: var(--paper-text); }
  .card-back .brand-tagline { font-size: 19px; color: var(--paper-text); margin-top: 6px; }
  .ghost-name {
    position: absolute; right: -10px; top: 40px;
    font-size: 260px; font-weight: 300; line-height: 1;
    letter-spacing: 10px;
    color: var(--ghost);
  }
</style>
</head>
<body>

<section class="card card-front" aria-label="Business card front">
  <div class="brand">
    <span class="brand-name">BRL</span>
    <span class="brand-tagline">Design and Productions</span>
  </div>

  <div class="divider"></div>

  <div class="contact">
    <p class="person-name">Daniel Hart</p>
    <p class="person-role">Manager</p>
    <ul class="contact-list">
      <li class="contact-item">
        <svg viewBox="0 0 16 16" aria-hidden="true"><path d="M3 1.5l2.5 2.5-1.5 1.8c.8 2 2.2 3.4 4.2 4.2l1.8-1.5 2.5 2.5-1.6 2.2C6.5 13 3 9.5 1 3.1z" fill="#2b2b2b"/></svg>
        +123 555 0148
      </li>
      <li class="contact-item">
        <svg viewBox="0 0 16 16" aria-hidden="true"><rect x="4" y="1" width="8" height="14" rx="1.5" fill="none" stroke="#2b2b2b" stroke-width="1.5"/><circle cx="8" cy="12.5" r="0.9" fill="#2b2b2b"/></svg>
        +123 555 0172
      </li>
      <li class="contact-item">
        <svg viewBox="0 0 16 16" aria-hidden="true"><rect x="1" y="3.5" width="14" height="9.5" fill="#2b2b2b"/><path d="M1 3.5l7 5.5 7-5.5" fill="none" stroke="#fff" stroke-width="1.2"/></svg>
        danielhart@mail.com
      </li>
      <li class="contact-item">
        <svg viewBox="0 0 16 16" aria-hidden="true"><rect x="1" y="2" width="14" height="9.5" fill="none" stroke="#2b2b2b" stroke-width="1.4"/><path d="M5.5 14.5h5M8 11.5v3" stroke="#2b2b2b" stroke-width="1.4"/></svg>
        www.brldesign.com
      </li>
    </ul>
  </div>

  <div class="address-band">Unit 4, Harbor Lane, Ashford, State, 40210</div>
</section>

<section class="card card-back" aria-label="Business card back">
  <span class="ghost-name" aria-hidden="true">BRL</span>
  <div class="brand">
    <span class="brand-name">BRL</span>
    <span class="brand-tagline">Design and Productions</span>
  </div>
</section>

</body>
</html>
```